Web design for insurance consultant. Target clients are (re)insurers, insurtech firms and vendor...

Need a crisp, modern website which will talk briefly about the firm and its principal founder. And, details around services offered for 3 different target clients: (1) re/insurance companies, (2) insurtech and IoT firms, and (3) vendors such as claims adjusting firms and home inspection firms supporting insurers

Target Market(s)

C-suite leaders of insurance companies, reinsurance companies, insurtech firms looking to innovate property insurance, and vendors selling to these insurance companies. Focus is property insurance in coastal, catastrophe-exposed regions of the US.

Coding

Coded - Design and coding required

Number of Pages Required

5+ page

Other font styles liked:
• not sure of font wanted - classic, but modern

Colors
0792cd
00a990

Requirements
Must have
• First box should use the attached "light bulb storm" picture as background.
• one change overall - remove "Get a quote" button - we do not sell to consumers, it's strictly B2B.
• For the 3 segments, use the pictures below. I could not find one I liked for "TPAs/Vendors", so welcome your suggestions.
• Want quotes in the boxes of each of the 3 market segments.
• Button on each of the 3 market segments would lead to content (not yet finished) that will explain in more detail the services to be provided to them.
Should not have
• don't want velkori plots or others showing location of business (waste of space, in my opinion)

```html
<!DOCTYPE html>
<html lang="en">
<head>
<meta charset="utf-8">
<title>Halvern Consulting – Insurance Consulting</title>
<link href="https://fonts.googleapis.com/css2?family=Lato:wght@400;700;900&display=swap" rel="stylesheet">
<style>
:root{
  --navy:#1a5a8c;
  --blue:#0792cd;
  --teal:#00a990;
  --teal-soft:#3bbfa0;
  --panel-left:#2d6793;
  --panel-right:#3d77a8;
  --ink:#2b2b2b;
  --muted:#666;
  --line:#dcdcdc;
  --light:#f7f7f7;
  --footer:#2c2c2c;
  --footer-text:#8a8a8a;
  --white:#fff;
}
*{box-sizing:border-box;margin:0;padding:0}
html,body{width:1200px;height:2583px;overflow:hidden}
body{position:relative;font-family:"Lato",sans-serif;color:var(--ink);background:var(--white)}
.abs{position:absolute}

/* header */
.brand{left:98px;top:34px;height:70px;display:flex;align-items:center;gap:14px}
.brand-dot{width:62px;height:62px;border-radius:50%;background:var(--navy)}
.brand-name{font-size:30px;font-weight:700;color:var(--navy);line-height:1}
.brand-name small{display:block;font-size:15px;font-weight:700;letter-spacing:3px;margin-top:4px}
.contact-line{top:22px;font-size:17px;display:flex;align-items:center;gap:12px;color:var(--ink)}
.nav{top:78px;left:598px;display:flex;gap:26px;font-size:14px;text-transform:uppercase;color:var(--ink)}
.btn{display:flex;align-items:center;justify-content:center;border-radius:40px;color:var(--white);font-weight:700;text-transform:uppercase}
.btn-contact{left:907px;top:69px;width:193px;height:38px;background:var(--teal);font-size:14px;font-weight:400}

/* hero */
.hero{left:0;top:133px;width:1200px;height:522px;background:radial-gradient(circle at 62% 30%,#c6d8e6 0%,#7d9db6 30%,#4a6b86 65%,#2f4a60 100%)}
.hero-title{left:112px;top:318px;font-size:38px;font-weight:700;color:var(--white)}
.hero-text{left:114px;top:380px;width:320px;font-size:14.5px;line-height:22px;color:var(--white)}

/* segments */
.segment{top:655px;width:400px;height:400px;color:var(--white);text-align:center}
.seg-1{left:0;background:linear-gradient(160deg,#3b78a6,var(--panel-left) 60%,#234f73)}
.seg-2{left:401px;background:var(--teal-soft)}
.seg-3{left:801px;width:399px;background:linear-gradient(160deg,#4a86b7,var(--panel-right) 60%,#2c5f8c)}
.tab{top:634px;width:210px;height:45px}
.tab svg{position:absolute;inset:0}
.tab span{position:relative;display:flex;height:100%;align-items:center;justify-content:center;font-size:21px;color:var(--navy)}
.quote-mark{position:absolute;left:0;right:0;top:72px;font-size:64px;font-weight:900;line-height:1}
.quote{position:absolute;left:50px;right:50px;font-size:14.5px;line-height:23.5px}
.quote cite{display:block;font-style:normal;font-weight:700;font-size:13.5px;margin-top:12px}
.btn-seg{top:1091px;width:176px;height:43px;font-size:13.5px;background:var(--teal)}
.btn-seg.alt{background:var(--navy)}

/* about */
.about-bg{left:60px;top:1185px;width:700px;height:560px;background:linear-gradient(90deg,#fbfbfb,#fff)}
.portrait-frame{left:207px;top:1265px;width:324px;height:469px;border:9px solid var(--navy)}
.portrait{left:220px;top:1218px;width:340px;height:505px;background:linear-gradient(180deg,#d9d9d9 0%,#545b66 45%,#2d323b 100%)}
.about-name{left:696px;top:1347px;font-size:36px;font-weight:700;color:#333}
.about-text{left:696px;top:1416px;width:370px;font-size:15.5px;line-height:24px;color:#555}
.btn-about{left:696px;top:1579px;width:316px;height:64px;background:var(--teal);font-size:20px;font-weight:400}

/* contact */
.contact{left:0;top:1819px;width:1200px;height:414px;background:var(--light)}
.contact-title{left:190px;top:1884px;font-size:31px;font-weight:700;color:#222}
.contact-text{left:190px;top:1946px;width:310px;font-size:11.5px;line-height:21px;color:#555}
.label{font-size:9px;letter-spacing:1.5px;color:#999;text-transform:uppercase}
.value{font-size:12px;color:#444}
.field{background:var(--white);border:1px solid var(--line);font-size:11px;color:#999;display:flex;align-items:center;gap:12px;padding-left:14px}
.field.msg{align-items:flex-start;padding-top:12px}
.btn-send{left:612px;top:2117px;width:141px;height:41px;background:var(--teal);font-size:10px;letter-spacing:3px}

/* footer */
.footer{left:0;top:2233px;width:1200px;height:350px;background:var(--footer)}
.f-head{top:2301px;font-size:10.5px;font-weight:700;letter-spacing:3px;color:var(--white);text-transform:uppercase}
.f-links{top:2335px;display:flex;flex-direction:column;gap:16px;font-size:11.5px;color:var(--footer-text)}
.newsletter{left:817px;top:2340px;width:207px;height:39px;border-radius:20px;background:#383838;font-size:11px;color:var(--footer-text);display:flex;align-items:center;padding-left:22px}
.news-btn{left:987px;top:2344px;width:32px;height:32px;border-radius:50%;background:var(--teal);display:flex;align-items:center;justify-content:center}
.copyright{left:184px;top:2500px;font-size:11.5px;color:#777}
</style>
</head>
<body>

<header>
  <div class="abs brand"><span class="brand-dot"></span><span class="brand-name">halvern<small>consulting</small></span></div>
  <div class="abs contact-line" style="left:680px">
    <svg width="18" height="18" viewBox="0 0 24 24"><path fill="#1a5a8c" d="M6.6 10.8a15 15 0 0 0 6.6 6.6l2.2-2.2c.3-.3.7-.4 1-.2 1.1.4 2.3.6 3.6.6.6 0 1 .4 1 1V20c0 .6-.4 1-1 1A17 17 0 0 1 3 4c0-.6.4-1 1-1h3.5c.6 0 1 .4 1 1 0 1.3.2 2.5.6 3.6.1.3 0 .7-.2 1z"/></svg>
    972 555 0148
  </div>
  <div class="abs contact-line" style="left:857px">
    <svg width="22" height="16" viewBox="0 0 22 16"><rect width="22" height="16" rx="1" fill="#1a5a8c"/><path d="M1 1l10 8 10-8" stroke="#fff" stroke-width="1.6" fill="none"/></svg>
    dale@halvernconsulting.com
  </div>
  <nav class="abs nav"><span>Home</span><span>About Us</span><span>Our Services</span></nav>
  <div class="abs btn btn-contact">Contact Us</div>
</header>

<section>
  <div class="abs hero" role="img" aria-label="Photo of a light bulb lying on its side with a storm and lightning inside the glass"></div>
  <h1 class="abs hero-title">Insurance Consulting</h1>
  <p class="abs hero-text">Proin luctus leo risus, in blandit lorem semper non. Donec semper dignissim sapien, in convallis ex pulvinar et.</p>
</section>

<section>
  <div class="abs segment seg-1" role="img" aria-label="Blue-tinted photo for reinsurers">
    <div class="quote-mark">&ldquo;</div>
    <p class="quote" style="top:128px">&ldquo;Halvern has a unique skill set in property cat that helped us refine our approach, particularly in the challenging Florida market. He was instrumental to us in distilling down our business plan, interactions and approvals with the Coastal Bureau, pricing and product development, and executing on our business plan.&rdquo;<cite>Founder and President, Insurance Company</cite></p>
  </div>
  <div class="abs segment seg-2" role="img" aria-label="Teal-tinted photo for insurtech and IoT">
    <div class="quote-mark" style="top:58px">&ldquo;</div>
    <p class="quote" style="top:107px;left:46px;right:46px">&ldquo;We didn't realize how hard insurance is. Dale's operational insights and suggestions across the organization (i.e., from submission/bind through to claims handling) accelerated our launch and build-out by a number of months. He was especially valuable in helping us work through operationalizing new technologies to make the process smoother, more efficient, and consumer-friendly.&rdquo;<cite>Founder and COO, Insurtech MGA</cite></p>
  </div>
  <div class="abs segment seg-3" role="img" aria-label="Blue-tinted photo of hands holding a house for vendors and TPAs">
    <div class="quote-mark" style="top:100px">&ldquo;</div>
    <p class="quote" style="top:155px;left:55px;right:45px">&ldquo;Halvern knows everybody in this space. As important as his connections were to us, he also provided huge value to us in preparing and responding to RFPs. He's expensive, but worth every penny!&rdquo;<cite>CEO, Third Party Administrator</cite></p>
  </div>

  <div class="abs tab" style="left:100px"><svg viewBox="0 0 210 45" preserveAspectRatio="none"><polygon points="18,0 210,0 192,45 0,45" fill="#fff"/></svg><span>(Re)Insurers</span></div>
  <div class="abs tab" style="left:490px"><svg viewBox="0 0 210 45" preserveAspectRatio="none"><polygon points="18,0 210,0 192,45 0,45" fill="#fff"/></svg><span>Insurtech / IoT</span></div>
  <div class="abs tab" style="left:875px;width:215px"><svg viewBox="0 0 215 45" preserveAspectRatio="none"><polygon points="18,0 215,0 197,45 0,45" fill="#fff"/></svg><span>Vendors and TPAs</span></div>

  <div class="abs btn btn-seg" style="left:110px">Learn More</div>
  <div class="abs btn btn-seg alt" style="left:510px">Learn More</div>
  <div class="abs btn btn-seg" style="left:910px">Learn More</div>
</section>

<section>
  <div class="abs about-bg"></div>
  <div class="abs portrait-frame"></div>
  <div class="abs portrait" role="img" aria-label="Portrait photo of the founder in a dark suit with arms crossed"></div>
  <h2 class="abs about-name">Dale Halvern</h2>
  <p class="abs about-text">Lorem ipsum dolor sit amet, consectetur adipiscing elit. Praesent vel porttitor metus. Pellentesque imperdiet hendrerit massa id efficitur. Sed eu blandit mauris, vel euismod nunc. Duis eros enim, facilisis et laoreet a, tincidunt vel justo. Aliquam erat volutpat.</p>
  <div class="abs btn btn-about">Learn More</div>
</section>

<section>
  <div class="abs contact"></div>
  <h2 class="abs contact-title">Contacts Us</h2>
  <p class="abs contact-text">Lorem ipsum dolor sit amet, consectetur adipiscing elit. Fusce sapien risus, congue vitae lectus a, lacinia posuere dui. Quisque sed viverra mauris.</p>
  <div class="abs label" style="left:190px;top:2052px">Email:</div>
  <div class="abs value" style="left:190px;top:2074px">dale@halvernconsulting.com</div>
  <div class="abs label" style="left:190px;top:2115px">Phone:</div>
  <div class="abs value" style="left:190px;top:2134px">+1 555-678-0192</div>

  <div class="abs field" style="left:612px;top:1891px;width:205px;height:40px">
    <svg width="11" height="12" viewBox="0 0 11 12"><circle cx="5.5" cy="3" r="3" fill="#999"/><path d="M0 12a5.5 5 0 0 1 11 0z" fill="#999"/></svg>Name</div>
  <div class="abs field" style="left:828px;top:1891px;width:206px;height:40px">
    <svg width="14" height="10" viewBox="0 0 14 10"><rect width="14" height="10" fill="#999"/><path d="M0 0l7 5 7-5" stroke="#fff" fill="none"/></svg>E-mail</div>
  <div class="abs field msg" style="left:612px;top:1945px;width:422px;height:157px">Your Message</div>
  <div class="abs btn btn-send">Send</div>
</section>

<footer>
  <div class="abs footer"></div>
  <div class="abs f-head" style="left:184px">Learn More</div>
  <div class="abs f-head" style="left:395px">Information</div>
  <div class="abs f-head" style="left:607px">Get in Touch</div>
  <div class="abs f-head" style="left:815px">Subscribe to Newsletter</div>
  <div class="abs f-links" style="left:184px"><span>Home</span><span>Services</span><span>blog</span><span>Testimonials</span></div>
  <div class="abs f-links" style="left:395px"><span>About Us</span><span>FAQs</span><span>Privacy Policy</span><span>Terms &amp; Conditions</span></div>
  <div class="abs f-links" style="left:607px"><span>Contact Us</span><span>Customer Service</span></div>
  <div class="abs newsletter">E-mail</div>
  <div class="abs news-btn"><svg width="14" height="10" viewBox="0 0 14 10"><rect x=".5" y=".5" width="13" height="9" fill="none" stroke="#fff"/><path d="M.5.5l6.5 5 6.5-5" stroke="#fff" fill="none"/></svg></div>
  <div class="abs copyright">© 2019 Halvern Consulting. All rights reserved.</div>
</footer>

</body>
</html>
```